One Page Magazine Ad for New Apartment in Calgary, AB Canada

We need a one page magazine ad for a new apartment community in Calgary, Alberta.

We pride ourselves in providing the highest level of customer service and the best amenities for our community.

COMMUNITY HIGHLIGHTS

- Brand new luxury apartment rental community in the exciting Calgary Beltline neighborhood
- 13 unique spacious floor plans fit for every lifestyle (1BR-1BATH, 2BR-1BATH & 2BR-2BATH)
- Professionally managed
- On-site staff during business hours to help you with any of your needs
- Pet-friendly community
- State of the art Fitness Facility
- 2 rooftop terraces outfitted with 8 Community Brimfield BBQs
- Great area for entertaining guests and a safe spot to take your dog out for some fresh air without leaving the building
- 2 resident lounges with multimedia suite, 60-inch TVs, Vexa Two, Silver Pin Arcade system, Poker table
- Great venues to host your next party, open 24/7 free to use and bookable by residents for free!
- Monthly resident events and parties hosted by the on-site staff
- Underground secured guest and resident parking available
- Electric Car Charging Stations
- Garbage & Recycling chutes on every floor
- Controlled Access/Building
- Gated Underground Parking Garage
- Adjacent to the Beltline neighborhood bike lane on 27th Avenue SW
- Elevators - Underground Secured Bike Storage and bike repair workstation
- On-site Maintenance
- Crate Keeper Package Management System
- Additional Storage Available
- Footsteps away from the local Fairmart Grocery and Fairmart Wine Store
- Minutes away from the new free leash dog park Wexley Park

APARTMENT AMENITIES

- Gourmet Kitchen with 4 piece Stainless Steel Appliances (Stove, Fridge, Microwave and Dishwasher)
- In suite dryer and washer
- Large Closets
- Patio/Balcony
- City and mountain views
- Ceramic Tile and Laminate Hardwood Flooring
- Quartz Counter-tops
- Roller Blinds for all Windows
- Walk-in Closets

For branding style, floor plans, amenities and photos please visit our website www.stayatthevorn.com

Target Market(s)

Young Adults and Recently Single Market

Industry/Entity Type

Real Estate

Font styles to use
Sans Serif

Colors
f37122

Requirements
Must have
• - Pictures of the community
• - Possibly use of a stock photo

```html
<!DOCTYPE html>
<html lang="en">
<head>
<meta charset="utf-8">
<title>The Vorn – Magazine Ad</title>
<link href="https://fonts.googleapis.com/css2?family=Open+Sans:ital,wght@0,400;0,600;0,700;1,400&display=swap" rel="stylesheet">
<style>
  :root {
    --backdrop: #e4e4e4;
    --paper: #ffffff;
    --red: #e31b37;
    --orange: #f37122;
    --orange-deep: #ef5a24;
    --charcoal: #4a4a4c;
    --ink: #2b2b2b;
    --light: #ffffff;
  }
  * { margin: 0; padding: 0; box-sizing: border-box; }
  html, body {
    width: 1200px; height: 862px; overflow: hidden;
    background: var(--backdrop);
    font-family: "Open Sans", Arial, sans-serif;
  }
  .ad-page {
    position: absolute; left: 300px; top: 16px;
    width: 600px; height: 830px;
    background: var(--paper);
    overflow: hidden;
    box-shadow: 0 6px 24px rgba(0,0,0,.18);
  }
  .photo { position: absolute; }
  .photo--building {
    left: 0; top: 0; width: 340px; height: 300px;
    background: linear-gradient(160deg, #8fb2d6 0%, #c9d5df 35%, #8a6a4e 62%, #3c3a3c 100%);
  }
  .photo--living {
    left: 345px; top: 0; width: 255px; height: 122px;
    background: linear-gradient(135deg, #e9e6e0 0%, #c9c3b8 55%, #2c8fa8 80%, #8b6c4c 100%);
  }
  .photo--bedroom {
    left: 345px; top: 127px; width: 255px; height: 120px;
    background: linear-gradient(160deg, #dfe3e8 0%, #b9bfc6 50%, #6b6e72 80%, #8fae3a 100%);
  }
  .photo--kitchen {
    left: 330px; top: 252px; width: 270px; height: 180px;
    background: linear-gradient(150deg, #f2f2f2 0%, #d7d8d9 45%, #9a9da1 75%, #4a4d52 100%);
  }
  .headline-band {
    position: absolute; left: 0; top: 212px; width: 360px; height: 86px;
    background: var(--red);
    color: var(--light);
    padding: 10px 16px;
    text-transform: uppercase;
    z-index: 3;
  }
  .headline-band h1 {
    font-size: 17px; font-weight: 600; line-height: 1.15; letter-spacing: .2px;
  }
  .headline-band p {
    font-size: 12px; font-weight: 400; line-height: 1.25;
  }
  .headline-band .headline-area { font-size: 16px; font-weight: 600; }
  .highlights {
    position: absolute; left: 0; top: 298px; width: 330px; height: 472px;
    background: linear-gradient(135deg, var(--orange) 0%, var(--orange-deep) 100%);
    padding: 12px 14px 10px 16px;
    color: var(--light);
  }
  .check-list { list-style: none; }
  .check-list li {
    position: relative; padding-left: 12px;
    font-size: 8.6px; line-height: 1.28; margin-bottom: 2.6px;
  }
  .check-list li::before {
    content: "\2713"; position: absolute; left: 0; top: 0; font-weight: 700;
  }
  .amenities-title {
    position: absolute; left: 330px; top: 432px; width: 270px; height: 34px;
    background: var(--charcoal); color: var(--light);
    font-size: 13px; font-weight: 600; letter-spacing: .6px;
    text-transform: uppercase; padding: 8px 14px;
  }
  .amenities {
    position: absolute; left: 330px; top: 466px; width: 270px; height: 150px;
    background: var(--red); color: var(--light);
    padding: 9px 12px 8px 14px;
  }
  .amenities .check-list li { font-size: 9.6px; line-height: 1.25; margin-bottom: 1.6px; }
  .amenities small { font-size: 7px; }
  .brand {
    position: absolute; left: 330px; top: 616px; width: 270px; height: 154px;
    display: flex; align-items: center; justify-content: center;
  }
  .brand-name {
    font-size: 24px; font-weight: 400; letter-spacing: 6px;
    color: var(--charcoal); text-transform: uppercase;
  }
  .contact-strip {
    position: absolute; left: 0; bottom: 0; width: 600px; height: 60px;
    background: var(--red); color: var(--light);
    display: flex; align-items: center; justify-content: space-between;
    padding: 0 16px;
  }
  .contact-item { display: flex; align-items: center; gap: 5px; font-size: 11px; }
  .contact-item--phone { font-size: 14px; font-weight: 700; }
  .contact-item svg { width: 13px; height: 13px; flex: none; }
</style>
</head>
<body>
<main class="ad-page">
  <div class="photo photo--building" role="img" aria-label="Photo of the tall apartment tower against a cloudy blue sky"></div>
  <div class="photo photo--living" role="img" aria-label="Photo of a bright living room with a teal sofa"></div>
  <div class="photo photo--bedroom" role="img" aria-label="Photo of a furnished bedroom with large window"></div>
  <div class="photo photo--kitchen" role="img" aria-label="Photo of a modern kitchen with stainless steel appliances"></div>

  <header class="headline-band">
    <h1>Brand new luxury apartment</h1>
    <p>Rental community in the exciting Calgary</p>
    <p class="headline-area">Beltline Neighborhood</p>
  </header>

  <section class="highlights">
    <ul class="check-list">
      <li>13 unique spacious floor plans fit for every lifestyle (1BR-1BATH, 2BR-1BATH &amp; 2BR-2BATH)</li>
      <li>Professionally managed</li>
      <li>On-site staff during business hours to help you with any of your needs</li>
      <li>Pet-friendly community</li>
      <li>State of the art Fitness Facility</li>
      <li>2 rooftop terraces outfitted with 8 Community Brimfield BBQs</li>
      <li>Great area for entertaining guests and a safe spot to take your dog out for some fresh air without leaving the building</li>
      <li>2 resident lounges with multimedia suite, 60-inch TVs, Vexa Two, Silver Pin Arcade system, Poker table</li>
      <li>Great venues to host your next party, open 24/7 free to use and bookable by residents for free!</li>
      <li>Monthly resident events and parties hosted by the on-site staff</li>
      <li>Underground secured guest and resident parking available</li>
      <li>Electric Car Charging Stations</li>
      <li>Garbage &amp; Recycling chutes on every floor</li>
      <li>Controlled Access/Building</li>
      <li>Gated Underground Parking Garage</li>
      <li>Adjacent to the Beltline neighborhood bike lane on 27th Avenue SW</li>
      <li>Elevators - Underground Secured Bike Storage and bike repair workstation</li>
      <li>On-site Maintenance</li>
      <li>Crate Keeper Package Management System</li>
      <li>Additional Storage Available</li>
      <li>Footsteps away from the local Fairmart Grocery and Fairmart Wine Store</li>
      <li>Minutes away from the new free leash dog park Wexley Park</li>
    </ul>
  </section>

  <h2 class="amenities-title">Apartment Amenities</h2>
  <section class="amenities">
    <ul class="check-list">
      <li>Gourmet Kitchen with 4 piece Stainless Steel Appliances <small>(Stove, Fridge, Microwave and Dishwasher)</small></li>
      <li>In suite dryer and washer</li>
      <li>Large Closets</li>
      <li>Patio/Balcony</li>
      <li>City and mountain views</li>
      <li>Ceramic Tile and Laminate Hardwood Flooring</li>
      <li>Quartz Counter-tops</li>
      <li>Roller Blinds for all Windows</li>
      <li>Walk-in Closets</li>
    </ul>
  </section>

  <div class="brand"><span class="brand-name">The Vorn</span></div>

  <footer class="contact-strip">
    <span class="contact-item">
      <svg viewBox="0 0 16 16" aria-hidden="true"><circle cx="8" cy="8" r="7" fill="none" stroke="#fff" stroke-width="1.4"/><ellipse cx="8" cy="8" rx="3" ry="7" fill="none" stroke="#fff" stroke-width="1.2"/><line x1="1" y1="8" x2="15" y2="8" stroke="#fff" stroke-width="1.2"/></svg>
      www.stayatthevorn.com
    </span>
    <span class="contact-item contact-item--phone">
      <svg viewBox="0 0 16 16" aria-hidden="true"><circle cx="8" cy="8" r="7" fill="none" stroke="#fff" stroke-width="1.4"/><path d="M5.5 4.5c.6-.4 1.1 0 1.3.6l.3.9c.1.4-.2.7-.5.9.4.9 1 1.6 1.9 2 .2-.3.6-.6 1-.5l.9.3c.6.2.9.8.5 1.3-.6.8-1.6.9-2.6.4-1.6-.8-2.8-2.1-3.4-3.7-.3-.9-.1-1.7.6-2.2z" fill="#fff"/></svg>
      (403) 555-0142
    </span>
    <span class="contact-item">
      <svg viewBox="0 0 16 16" aria-hidden="true"><path d="M8 1.5a4.5 4.5 0 0 0-4.5 4.5c0 3.4 4.5 8.5 4.5 8.5s4.5-5.1 4.5-8.5A4.5 4.5 0 0 0 8 1.5z" fill="none" stroke="#fff" stroke-width="1.4"/><circle cx="8" cy="6" r="1.6" fill="#fff"/></svg>
      1480 - 9th Avenue SW Calgary, AB T3C 2K7
    </span>
  </footer>
</main>
</body>
</html>
```